Breezeway Masters Business Card Design

Design new, 2 sides, business cards for a residential and light commercial heating, air conditioning contractor.

Target Market(s)

Homeowners, small businesses

Industry/Entity Type

Business

Contact Information for Business Card

Dominic Halvorsen
Phone - 862-415-2763
Email
Address - PO box 648
Larkfield NJ 07990
Website - www.BreezewayMastersLLC.example

Requirements
Must have
• logo, company colors, standard size with no die cut, so I can use nimbo press

```html
<!DOCTYPE html>
<html lang="en">
<head>
<meta charset="utf-8">
<title>Breezeway Masters – Business Card</title>
<link rel="stylesheet" href="https://fonts.googleapis.com/css2?family=Tinos:wght@700&display=swap">
<style>
  :root {
    --backdrop: #d9d9d9;
    --card-dark: #2c2a2a;
    --cream: #fbe99a;
    --cream-text: #f7e6a2;
    --brick: #a3293a;
    --orange: #ef8a1f;
    --ink: #2a2626;
  }
  * { margin: 0; padding: 0; box-sizing: border-box; }
  html, body {
    width: 1102px;
    height: 1200px;
    overflow: hidden;
    background: var(--backdrop);
    font-family: "Tinos", "Times New Roman", serif;
    font-weight: 700;
  }
  .card {
    position: absolute;
    box-shadow: 0 6px 14px rgba(0,0,0,0.25);
    overflow: hidden;
  }
  .card-front {
    left: 157px; top: 95px;
    width: 777px; height: 460px;
    background: var(--card-dark);
    display: flex;
    align-items: center;
    justify-content: center;
  }
  .company-name {
    color: var(--cream-text);
    font-size: 76px;
    line-height: 1.05;
    text-align: center;
    letter-spacing: 1px;
  }
  .card-back {
    left: 164px; top: 619px;
    width: 776px; height: 470px;
    background: var(--card-dark);
  }
  .back-divider {
    position: absolute;
    left: 0; top: 0;
    width: 776px; height: 470px;
  }
  .contact-line {
    position: absolute;
    left: 0; width: 100%;
    display: flex;
    align-items: center;
    justify-content: center;
    gap: 12px;
    white-space: nowrap;
  }
  .contact-line svg { flex: none; }
  .person-name {
    top: 62px;
    font-size: 25px;
    color: var(--cream-text);
    letter-spacing: 0.5px;
    word-spacing: 4px;
  }
  .phone { top: 128px; font-size: 28px; color: var(--cream-text); }
  .email { top: 190px; font-size: 23px; color: var(--cream-text); }
  .website { top: 328px; font-size: 28px; color: var(--ink); }
  .address { top: 390px; font-size: 28px; color: var(--ink); }
</style>
</head>
<body>

<section class="card card-front" aria-label="Card front">
  <h1 class="company-name">Breezeway<br>Masters</h1>
</section>

<section class="card card-back" aria-label="Card back">
  <svg class="back-divider" viewBox="0 0 776 470" aria-hidden="true">
    <path fill="var(--brick)" d="M0,203 C150,216 300,228 388,286 C476,228 626,216 776,203 L776,470 L0,470 Z"/>
    <path fill="var(--orange)" d="M0,212 C150,225 300,237 388,295 C476,237 626,225 776,212 L776,470 L0,470 Z"/>
    <path fill="var(--cream)" d="M0,217 C150,230 300,242 388,300 C476,242 626,230 776,217 L776,470 L0,470 Z"/>
  </svg>

  <p class="contact-line person-name">DOMINIC HALVORSEN</p>

  <p class="contact-line phone">
    <svg width="20" height="26" viewBox="0 0 20 26" aria-hidden="true">
      <path fill="var(--cream-text)" d="M5 1 L9 6 L6.5 9 C7.5 13 9.5 16 12.5 18 L15 15.5 L19 20 L16 24 C9 24 2 14 2 5 Z"/>
    </svg>
    862-415-2763
  </p>

  <p class="contact-line email">
    <svg width="24" height="18" viewBox="0 0 24 18" aria-hidden="true">
      <rect x="1" y="3" width="22" height="14" fill="var(--cream-text)"/>
      <path d="M1 3 L12 11 L23 3" fill="none" stroke="var(--card-dark)" stroke-width="2"/>
    </svg>
    name@BreezewayMastersLLC.example
  </p>

  <p class="contact-line website">
    <svg width="26" height="26" viewBox="0 0 26 26" aria-hidden="true">
      <circle cx="13" cy="13" r="12" fill="var(--brick)"/>
      <g fill="none" stroke="var(--cream)" stroke-width="1.4">
        <ellipse cx="13" cy="13" rx="5" ry="11"/>
        <line x1="2" y1="13" x2="24" y2="13"/>
        <line x1="13" y1="2" x2="13" y2="24"/>
        <path d="M4 7 H22 M4 19 H22"/>
      </g>
    </svg>
    www.BreezewayMastersLLC.example
  </p>

  <p class="contact-line address">
    <svg width="28" height="24" viewBox="0 0 28 24" aria-hidden="true">
      <path fill="var(--brick)" d="M14 1 L27 9 L1 9 Z"/>
      <rect x="3" y="10" width="22" height="13" fill="var(--brick)"/>
      <rect x="8" y="13" width="12" height="6" fill="var(--cream)"/>
    </svg>
    PO box 648,&nbsp; Larkfield NJ 07990
  </p>
</section>

</body>
</html>
```